Create banners that convert viewers into buyers!

We provide Online Marketing Solutions for small to medium size businesses from web design, Local SEO, Pay-Per-Click, Social Media and Content Marketing. We've been helping local businesses since 2009 and offer a very high level of service that is rarely matched.

Really like to stay colors of logo like banner ad ideas 2 sample.

Would also like to use a photo of a responsive web design as attached image. (you may use a different layout as image provided may be to big for some dimensions)

Sizes needed:
728x90
300x250
480x60

Add Slogan: We Drive Traffic & Phone Calls!

Slogan: We Drive Phone Calls & Conversions

Target Market(s)

Small to Medium Size businesses: Main businesses we work with are Home Improvement, Lawyers & Physicians

Industry/Entity Type

Marketing

```html
<!DOCTYPE html>
<html lang="en">
<head>
<meta charset="utf-8">
<title>Clearpath Marketing – Banner Set</title>
<link rel="stylesheet" href="https://fonts.googleapis.com/css2?family=Oswald:wght@500;600&family=Montserrat:wght@600&family=Tinos:wght@700&family=Arimo:wght@400&display=swap">
<style>
  :root {
    --page-bg: #e5eef8;
    --brand-blue: #1d64b4;
    --panel-dark: #1f2226;
    --panel-darker: #111315;
    --light-top: #cde2f5;
    --light-bottom: #eef5fc;
    --ink: #1e2a36;
    --white: #ffffff;
    --screen-a: #4a5560;
    --screen-b: #c9452f;
  }
  * { box-sizing: border-box; margin: 0; padding: 0; }
  html, body { width: 1200px; height: 715px; overflow: hidden; }
  body { background: var(--page-bg); position: relative; font-family: "Arimo", sans-serif; }

  /* Horizontal leaderboard layout (1103 x 139) */
  .leaderboard {
    position: absolute; width: 1103px; height: 139px;
    background: var(--panel-dark); border: 1px solid #3a3f45; overflow: hidden;
  }
  .leaderboard--large { left: 45px; top: 27px; }
  .leaderboard--small { left: 433px; top: 182px; transform: scale(0.648, 0.655); transform-origin: 0 0; }

  .leaderboard .brand-panel {
    position: absolute; left: 0; top: 0; width: 250px; height: 100%;
    background: linear-gradient(180deg, var(--light-top), var(--light-bottom));
    text-align: center;
  }
  .brand-mark { display: inline-flex; align-items: center; gap: 6px; color: var(--brand-blue);
    font-family: "Montserrat", sans-serif; font-weight: 600; }
  .brand-mark .dot { width: 9px; height: 9px; border-radius: 50%; background: var(--brand-blue); }
  .leaderboard .brand-mark { margin-top: 40px; font-size: 27px; letter-spacing: 0.5px; }
  .leaderboard .site-url { position: absolute; left: 0; right: 0; bottom: 28px; font-size: 18px; color: var(--ink); }

  .leaderboard .slogan-badge { position: absolute; left: 238px; top: 0; width: 370px; height: 139px; }
  .leaderboard .slogan-text {
    position: absolute; left: 238px; top: 0; width: 370px; height: 139px;
    display: flex; flex-direction: column; justify-content: center; align-items: center;
    font-family: "Oswald", sans-serif; font-weight: 600; color: var(--white);
    font-size: 33px; line-height: 1.05; text-transform: uppercase; letter-spacing: 0.5px;
  }

  .leaderboard .services-shape { position: absolute; left: 612px; top: 0; width: 268px; height: 139px; }
  .leaderboard .service-list {
    position: absolute; left: 628px; top: 18px; list-style: none;
    font-family: "Tinos", serif; font-weight: 700; color: var(--white); font-size: 19px; line-height: 21px;
  }
  .service-list li { display: flex; align-items: center; gap: 8px; }
  .service-list svg { width: 15px; height: 15px; flex: none; }

  .leaderboard .device-area {
    position: absolute; left: 885px; top: 12px; width: 205px; height: 115px;
    background: linear-gradient(180deg, var(--screen-a) 0%, #2b3138 55%, var(--screen-b) 100%);
    border-radius: 4px; opacity: 0.9;
  }

  /* Medium rectangle (455 x 379) */
  .rectangle {
    position: absolute; left: 45px; top: 286px; width: 455px; height: 379px;
    background: var(--panel-dark); border: 1px solid #3a3f45; overflow: hidden;
  }
  .rectangle .brand-panel {
    position: absolute; left: 0; top: 0; width: 236px; height: 310px;
    background: linear-gradient(180deg, var(--light-top), var(--light-bottom));
    text-align: center;
  }
  .rectangle .brand-stack { margin-top: 24px; color: var(--brand-blue);
    font-family: "Montserrat", sans-serif; font-weight: 600; line-height: 1; }
  .rectangle .brand-stack .name { font-size: 30px; }
  .rectangle .brand-stack .sub { font-size: 12px; letter-spacing: 5px; margin-top: 6px; }
  .rectangle .slogan-badge { position: absolute; left: 6px; top: 100px; width: 232px; height: 212px; }
  .rectangle .slogan-text {
    position: absolute; left: 6px; top: 100px; width: 232px; height: 200px;
    display: flex; flex-direction: column; justify-content: center; align-items: center;
    font-family: "Oswald", sans-serif; font-weight: 600; color: var(--white);
    text-transform: uppercase; line-height: 1.02;
  }
  .rectangle .slogan-text .lead { font-size: 27px; }
  .rectangle .slogan-text .main { font-size: 40px; }
  .rectangle .url-strip {
    position: absolute; left: 0; top: 312px; width: 236px; height: 67px;
    background: var(--panel-darker); display: flex; align-items: center; justify-content: center;
    color: var(--white); font-size: 19px;
  }
  .rectangle .device-area {
    position: absolute; left: 236px; top: 0; width: 219px; height: 144px;
    background: linear-gradient(180deg, var(--light-bottom), #b9c4cf 45%, var(--screen-a) 70%, var(--screen-b) 100%);
  }
  .rectangle .service-list {
    position: absolute; left: 252px; top: 154px; list-style: none;
    font-family: "Oswald", sans-serif; font-weight: 500; color: var(--white); font-size: 18px; line-height: 27px;
    text-transform: uppercase;
  }
  .rectangle .service-list .chevron { color: var(--white); margin-right: 4px; font-size: 13px; }
  .rectangle .cta-button {
    position: absolute; left: 240px; top: 312px; width: 208px; height: 46px;
    background: var(--brand-blue); display: flex; align-items: center; justify-content: center;
    color: var(--white); font-family: "Oswald", sans-serif; font-weight: 500;
    font-size: 22px; text-transform: uppercase; border: 3px solid var(--light-bottom);
  }

  /* Stand-alone brand lockup */
  .brand-lockup {
    position: absolute; left: 560px; top: 462px; width: 600px; text-align: center;
    color: var(--brand-blue); font-family: "Montserrat", sans-serif; font-weight: 600; line-height: 1;
  }
  .brand-lockup .name { font-size: 74px; letter-spacing: 2px; }
  .brand-lockup .sub { font-size: 26px; letter-spacing: 16px; margin-top: 12px; }
</style>
</head>
<body>

<svg width="0" height="0" style="position:absolute">
  <defs>
    <linearGradient id="badgeFill" x1="0" y1="0" x2="0" y2="1">
      <stop offset="0" stop-color="#2a82de"/>
      <stop offset="1" stop-color="#0b3f90"/>
    </linearGradient>
    <symbol id="tick" viewBox="0 0 16 16">
      <circle cx="8" cy="8" r="8" fill="#2a7fe0"/>
      <path d="M4.3 8.3l2.4 2.4 5-5" fill="none" stroke="#fff" stroke-width="2"/>
    </symbol>
  </defs>
</svg>

<!-- 728 x 90 -->
<section class="leaderboard leaderboard--large">
  <div class="brand-panel">
    <div class="brand-mark"><span class="dot"></span>CLEARPATH</div>
    <div class="site-url">www.SiteName.com</div>
  </div>
  <svg class="services-shape" viewBox="0 0 268 139"><polygon points="0,10 236,10 266,69 236,129 0,129" fill="#111315"/></svg>
  <svg class="slogan-badge" viewBox="0 0 370 139"><polygon points="30,4 340,4 368,69 340,135 30,135 2,69" fill="url(#badgeFill)" stroke="#0a2c66" stroke-width="3"/></svg>
  <div class="slogan-text"><span>We Drive</span><span>Traffic &amp;</span><span>Phone Calls!</span></div>
  <ul class="service-list">
    <li><svg><use href="#tick"/></svg>Web Design</li>
    <li><svg><use href="#tick"/></svg>Local SEO</li>
    <li><svg><use href="#tick"/></svg>Pay-Per-Click</li>
    <li><svg><use href="#tick"/></svg>Social Media</li>
    <li><svg><use href="#tick"/></svg>Content Marketing</li>
  </ul>
  <div class="device-area" role="img" aria-label="Responsive website shown on desktop, laptop, tablet and phone"></div>
</section>

<!-- 480 x 60 -->
<section class="leaderboard leaderboard--small">
  <div class="brand-panel">
    <div class="brand-mark"><span class="dot"></span>CLEARPATH</div>
    <div class="site-url">www.SiteName.com</div>
  </div>
  <svg class="services-shape" viewBox="0 0 268 139"><polygon points="0,10 236,10 266,69 236,129 0,129" fill="#111315"/></svg>
  <svg class="slogan-badge" viewBox="0 0 370 139"><polygon points="30,4 340,4 368,69 340,135 30,135 2,69" fill="url(#badgeFill)" stroke="#0a2c66" stroke-width="3"/></svg>
  <div class="slogan-text"><span>We Drive</span><span>Traffic &amp;</span><span>Phone Calls!</span></div>
  <ul class="service-list">
    <li><svg><use href="#tick"/></svg>Web Design</li>
    <li><svg><use href="#tick"/></svg>Local SEO</li>
    <li><svg><use href="#tick"/></svg>Pay-Per-Click</li>
    <li><svg><use href="#tick"/></svg>Social Media</li>
    <li><svg><use href="#tick"/></svg>Content Marketing</li>
  </ul>
  <div class="device-area" role="img" aria-label="Responsive website shown on desktop, laptop, tablet and phone"></div>
</section>

<!-- 300 x 250 -->
<section class="rectangle">
  <div class="brand-panel">
    <div class="brand-stack">
      <div class="name">CLEARPATH</div>
      <div class="sub">MARKETING</div>
    </div>
  </div>
  <div class="device-area" role="img" aria-label="Responsive website shown on desktop, tablet and phone"></div>
  <svg class="slogan-badge" viewBox="0 0 232 212"><polygon points="20,3 212,3 230,22 230,186 116,209 2,186 2,22" fill="url(#badgeFill)" stroke="#0a2c66" stroke-width="3"/></svg>
  <div class="slogan-text"><span class="lead">We Drive</span><span class="main">Traffic &amp;</span><span class="main">Phone</span><span class="main">Calls!</span></div>
  <div class="url-strip">www.SiteName.com</div>
  <ul class="service-list">
    <li><span class="chevron">&#10095;</span>Web Design</li>
    <li><span class="chevron">&#10095;</span>Local SEO</li>
    <li><span class="chevron">&#10095;</span>Pay-Per-Click</li>
    <li><span class="chevron">&#10095;</span>Social Media</li>
    <li><span class="chevron">&#10095;</span>Contect Marketing</li>
  </ul>
  <div class="cta-button">Know More</div>
</section>

<!-- Brand lockup -->
<div class="brand-lockup">
  <div class="name">CLEARPATH</div>
  <div class="sub">MARKETING</div>
</div>

</body>
</html>
```